Kivora - a fintech company - business card

We need a business card design for our Payments Technology company in Sydney, Australia. We provide business with payment solutions expanding across EFTPOS machines, online payment gateways and mobile payment solutions. We would like to see designs that are clean, classy and professional.
Target Market(s)
Business professionals, executives, c-suite
Industry/Entity Type
Fintech
Contact Information for Business Card
Will be on 400gsm. Logo will most likely be spot gloss unless designer recommends otherwise.
Font styles to use
Sans Serif
Requirements
Must have
- We need our website (kivora.com.au), email (contact@kivora.com.au), mobile (0455 806 274) and direct phone number (02 7391 5082) to feature on the card along with our logo (attached) and the words "EFTPOS | ONLINE | MOBILE"
- Font = Roboto

```html
<!DOCTYPE html>
<html lang="en">
<head>
<meta charset="utf-8">
<title>Kivora – Business Card</title>
<link href="https://fonts.googleapis.com/css2?family=Roboto:wght@400;500;700&display=swap" rel="stylesheet">
<style>
  :root {
    --brand-blue: #155f92;
    --ink-grey: #6d6e70;
    --text-grey: #4a4a4a;
    --paper: #ffffff;
    --backdrop: #1f1f21;
  }
  * { margin: 0; padding: 0; box-sizing: border-box; }
  html, body {
    width: 1200px; height: 801px; overflow: hidden;
    background: var(--backdrop);
    font-family: "Roboto", Arial, sans-serif;
  }
  .stage {
    width: 1200px; height: 801px;
    display: flex; flex-direction: column;
    align-items: center; justify-content: center; gap: 40px;
  }
  .card {
    position: relative;
    width: 560px; height: 340px;
    overflow: hidden;
  }
  /* Back side */
  .card--back { background: var(--brand-blue); color: var(--paper); }
  .back-brand {
    position: absolute; right: 46px; bottom: 44px; text-align: left;
  }
  .back-brand__name {
    font-weight: 700; font-size: 38px; letter-spacing: 0.5px; line-height: 1;
  }
  .back-brand__tagline {
    margin-top: 6px; font-size: 13.5px; font-weight: 400; letter-spacing: 0.3px;
  }
  /* Front side */
  .card--front { background: var(--paper); }
  .front-logo {
    position: absolute; right: 56px; top: 74px;
    display: flex; flex-direction: column; align-items: center; gap: 12px;
  }
  .front-logo__dot {
    width: 74px; height: 74px; border-radius: 50%; background: var(--brand-blue);
  }
  .front-logo__name {
    font-weight: 700; font-size: 34px; color: var(--ink-grey); letter-spacing: 0.5px; line-height: 1;
  }
  .person {
    position: absolute; left: 40px; top: 158px;
  }
  .person__name {
    font-weight: 700; font-size: 21px; color: var(--brand-blue); letter-spacing: 0.3px; line-height: 1.1;
  }
  .person__role {
    font-size: 13.5px; color: var(--ink-grey); margin-top: 1px;
  }
  .contacts {
    list-style: none; margin-top: 12px;
  }
  .contacts__item {
    display: flex; align-items: center; gap: 9px;
    font-size: 13px; color: var(--text-grey); line-height: 19px;
  }
  .contacts__icon { width: 11px; height: 11px; fill: var(--brand-blue); flex: none; }
  .web-band {
    position: absolute; left: 0; bottom: 20px;
    width: 470px; height: 30px;
    background: var(--brand-blue); color: var(--paper);
    display: flex; align-items: center; padding-left: 40px;
    font-size: 13px; letter-spacing: 2.6px;
  }
  .band-dot {
    position: absolute; right: 40px; bottom: 23px;
    width: 24px; height: 24px; border-radius: 50%; background: var(--brand-blue);
  }
</style>
</head>
<body>
<main class="stage">
  <section class="card card--back" aria-label="Card back">
    <div class="back-brand">
      <div class="back-brand__name">KIVORA</div>
      <div class="back-brand__tagline">EFTPOS | ONLINE | MOBILE</div>
    </div>
  </section>

  <section class="card card--front" aria-label="Card front">
    <div class="front-logo">
      <span class="front-logo__dot"></span>
      <span class="front-logo__name">KIVORA</span>
    </div>

    <div class="person">
      <div class="person__name">DANIEL REYES</div>
      <div class="person__role">CEO/FOUNDER</div>
      <ul class="contacts">
        <li class="contacts__item">
          <svg class="contacts__icon" viewBox="0 0 24 24"><path d="M6.6 10.8a15.1 15.1 0 0 0 6.6 6.6l2.2-2.2a1 1 0 0 1 1-.25 11.4 11.4 0 0 0 3.6.57 1 1 0 0 1 1 1V20a1 1 0 0 1-1 1A17 17 0 0 1 3 4a1 1 0 0 1 1-1h3.5a1 1 0 0 1 1 1c0 1.25.2 2.45.57 3.57a1 1 0 0 1-.25 1z"/></svg>
          02 7391 5082
        </li>
        <li class="contacts__item">
          <svg class="contacts__icon" viewBox="0 0 24 24"><path d="M7 1h10a2 2 0 0 1 2 2v18a2 2 0 0 1-2 2H7a2 2 0 0 1-2-2V3a2 2 0 0 1 2-2zm0 3v15h10V4zm5 16.2a.9.9 0 1 0 0 1.8.9.9 0 0 0 0-1.8z"/></svg>
          0455 806 274
        </li>
        <li class="contacts__item">
          <svg class="contacts__icon" viewBox="0 0 24 24"><path d="M2 5h20v14H2zm2 2v.4l8 5.2 8-5.2V7zm0 2.8V17h16V9.8l-8 5.2z"/></svg>
          contact@kivora.com.au
        </li>
      </ul>
    </div>

    <div class="web-band">www.kivora.com.au</div>
    <span class="band-dot"></span>
  </section>
</main>
</body>
</html>
```